Podcast Graphics For Internet Business Building Podcast

We need new podcast graphics.
1400x1400
300dpi

Needs to include text "Quiet Harbor Ledger Hour" as the podcast title and "Creative Internet Income Strategies" as a subtitle.

We like blue and grey as our main colors, but are open to other schemes.

Please see attached image for an example of podcast graphics we like. While we prefer a more plain look, it would be nice to have a subtle hint related to a "machine" in the background. Something like a pencil sketch of cogs like on the Quiet Harbor Ledger 10 book cover (attached image).

Target Market(s)

online entrepreneurs or those who want to start an online business

Font styles to use
Sans Serif

Colors
0455a3
3277b5

Requirements
Must have
• Text noted in project description
Should not have
• No money symbols or flashy "make money" type things.

```html
<!DOCTYPE html>
<html lang="en">
<head>
<meta charset="utf-8">
<title>Quiet Harbor Ledger Hour — Podcast Cover</title>
<link rel="stylesheet" href="https://fonts.googleapis.com/css2?family=Cabin:wght@400;700&display=swap">
<style>
  :root {
    --red-core: #f31414;
    --red-mid: #d40606;
    --red-edge: #9e0000;
    --ink-white: #ffffff;
    --cog-glow: rgba(255, 255, 255, 0.55);
    --cog-fade: rgba(255, 255, 255, 0);
  }
  html, body {
    margin: 0;
    padding: 0;
    width: 1200px;
    height: 1200px;
    overflow: hidden;
    background: var(--red-edge);
  }
  .cover {
    position: relative;
    width: 1200px;
    height: 1200px;
    overflow: hidden;
    background: radial-gradient(circle at 30% 36%, var(--red-core) 0%, var(--red-mid) 38%, var(--red-edge) 100%);
    font-family: "Cabin", sans-serif;
  }
  .cog-layer {
    position: absolute;
    inset: 0;
    width: 1200px;
    height: 1200px;
  }
  .show-title {
    position: absolute;
    left: 58px;
    top: 40px;
    margin: 0;
    color: var(--ink-white);
    font-family: "Cabin", sans-serif;
    font-weight: 700;
    font-size: 172px;
    line-height: 175px;
    letter-spacing: 1px;
    text-transform: uppercase;
    text-shadow: 0 2px 3px rgba(0, 0, 0, 0.25);
  }
  .show-title span { display: block; }
  .show-tagline {
    position: absolute;
    left: 80px;
    top: 800px;
    margin: 0;
    color: var(--ink-white);
    font-family: "Cabin", sans-serif;
    font-weight: 400;
    font-size: 49px;
    letter-spacing: 0.5px;
  }
</style>
</head>
<body>
<main class="cover">
  <svg class="cog-layer" viewBox="0 0 1200 1200" xmlns="http://www.w3.org/2000/svg">
    <defs>
      <radialGradient id="cogFill">
        <stop offset="0%" stop-color="var(--cog-glow)"/>
        <stop offset="70%" stop-color="rgba(255,255,255,0.35)"/>
        <stop offset="100%" stop-color="var(--cog-fade)"/>
      </radialGradient>
    </defs>
    <g class="cog-areas">
      <circle cx="998" cy="270" r="92" fill="url(#cogFill)" role="img" aria-label="Small white cog wheel"/>
      <circle cx="1200" cy="532" r="150" fill="url(#cogFill)" role="img" aria-label="Large white cog wheel partly off the edge"/>
      <circle cx="1095" cy="832" r="175" fill="url(#cogFill)" role="img" aria-label="Large white spoked cog wheel"/>
      <circle cx="180" cy="952" r="60" fill="url(#cogFill)" role="img" aria-label="Small white cog wheel"/>
      <circle cx="450" cy="1102" r="180" fill="url(#cogFill)" role="img" aria-label="Large white spoked cog wheel at the bottom"/>
    </g>
    <g class="motion-dots" fill="var(--ink-white)">
      <circle cx="885" cy="705" r="12"/>
      <circle cx="900" cy="773" r="8"/>
    </g>
    <g class="motion-arcs" fill="none" stroke="var(--ink-white)" stroke-width="2" stroke-dasharray="10 8">
      <path d="M240 1010 Q420 880 600 930 Q660 1010 635 1118"/>
      <path d="M922 920 Q960 1010 1020 1050"/>
    </g>
    <path class="motion-arrowhead" d="M627 1116 L635 1128 L643 1116" fill="none" stroke="var(--ink-white)" stroke-width="2"/>
  </svg>

  <h1 class="show-title">
    <span>Quiet</span>
    <span>Harbor</span>
    <span>Ledger</span>
    <span>Hour</span>
  </h1>
  <p class="show-tagline">Creative Internet Income Strategies</p>
</main>
</body>
</html>
```